Business Card Design

We need a business card design for a new company called Riverbend Advisory, LLC. We are a project management and software engineering consulting company. We prefer to use blues but am open to any colors. We would like out design to show strength and creativity.

I've uploaded new logo designs to the project.  Please use these logo designs for the business card. Thanks!

Industry/Entity Type

Software

Contact Information for Business Card

Daniel Whitford
Consultant
Owner

Riverbend Advisory, LLC

2716 5th St. S #4372
Arlington, VA 22198

703-555-0187
dwhitford@rvbadv.example
www.rvbadv.example

```html
<!DOCTYPE html>
<html lang="en">
<head>
<meta charset="utf-8">
<title>Riverbend Advisory – Business Card</title>
<link href="https://fonts.googleapis.com/css2?family=Arimo:wght@400;700&display=swap" rel="stylesheet">
<style>
  :root {
    --stage: #dcddde;
    --blue-light: #22719f;
    --blue-deep: #0b3d69;
    --navy: #0c3a5e;
    --red: #c0332a;
    --white: #ffffff;
    --ink: #0f3a63;
    --card-edge: #9aa0a6;
  }
  * { margin: 0; padding: 0; box-sizing: border-box; }
  html, body { width: 1200px; height: 1200px; overflow: hidden; }
  body {
    background: radial-gradient(circle at 50% 45%, #f1f1f2 0%, var(--stage) 70%, #c9cacc 100%);
    font-family: "Arimo", Arial, sans-serif;
    position: relative;
  }
  .card {
    position: absolute;
    left: 228px;
    width: 742px;
    height: 423px;
    overflow: hidden;
  }
  /* Front */
  .card-front {
    top: 167px;
    background: radial-gradient(ellipse at 50% 52%, var(--blue-light) 0%, #16578a 45%, var(--blue-deep) 100%);
    color: var(--white);
  }
  .front-brand {
    position: absolute;
    top: 138px;
    left: 0; right: 0;
    text-align: center;
  }
  .front-brand .brand-name {
    display: inline-flex;
    align-items: center;
    gap: 16px;
    font-size: 50px;
    font-weight: 700;
    letter-spacing: 1px;
    color: var(--white);
  }
  .brand-dot {
    width: 22px; height: 22px;
    border-radius: 50%;
    background: currentColor;
    display: inline-block;
  }
  .services {
    position: absolute;
    top: 270px;
    left: 0; right: 0;
    display: flex;
    justify-content: center;
    align-items: center;
    font-size: 19px;
  }
  .services .divider {
    width: 1.5px; height: 34px;
    background: var(--white);
    margin: 0 10px;
  }
  .front-web {
    position: absolute;
    top: 388px;
    left: 0; right: 0;
    display: flex;
    justify-content: center;
    align-items: center;
    gap: 5px;
    font-size: 17px;
    color: var(--red);
  }
  /* Back */
  .card-back {
    top: 601px;
    background: var(--white);
    border: 1px solid var(--card-edge);
  }
  .back-brand {
    position: absolute;
    left: 46px;
    top: 72px;
    display: flex;
    align-items: center;
    gap: 12px;
    font-size: 34px;
    font-weight: 700;
    color: var(--ink);
  }
  .back-brand .brand-dot { width: 16px; height: 16px; }
  .person {
    position: absolute;
    left: 84px;
    top: 203px;
    color: var(--ink);
  }
  .person-name { font-size: 19px; font-weight: 700; line-height: 1.15; }
  .person-title { font-size: 17px; line-height: 1.15; }
  .contact {
    position: absolute;
    right: 20px;
    top: 220px;
    list-style: none;
    color: var(--ink);
    font-size: 17px;
    text-align: right;
  }
  .contact li {
    display: flex;
    justify-content: flex-end;
    align-items: flex-start;
    gap: 6px;
    line-height: 20px;
  }
  .contact li + li { margin-top: 0; }
  .contact .email { margin-top: 6px; }
  .contact svg { flex: none; margin-top: 2px; }
  .back-bands { position: absolute; left: 0; top: 0; }
  .back-web {
    position: absolute;
    left: 274px; right: 0;
    top: 348px;
    height: 40px;
    display: flex;
    justify-content: center;
    align-items: center;
    gap: 6px;
    color: var(--white);
    font-size: 17px;
  }
</style>
</head>
<body>

<section class="card card-front" aria-label="Card front">
  <div class="front-brand">
    <span class="brand-name"><span class="brand-dot"></span>RIVERBEND ADVISORY</span>
  </div>
  <p class="services">
    <span>Project management</span>
    <span class="divider"></span>
    <span>Software engineering</span>
  </p>
  <p class="front-web">
    <svg width="22" height="22" viewBox="0 0 22 22" aria-hidden="true">
      <circle cx="11" cy="11" r="10" fill="var(--red)"/>
      <g fill="none" stroke="#fff" stroke-width="1.2">
        <circle cx="11" cy="11" r="6.5"/>
        <ellipse cx="11" cy="11" rx="3" ry="6.5"/>
        <line x1="4.5" y1="11" x2="17.5" y2="11"/>
        <line x1="5.5" y1="7.5" x2="16.5" y2="7.5"/>
        <line x1="5.5" y1="14.5" x2="16.5" y2="14.5"/>
      </g>
    </svg>
    www.rvbadv.example
  </p>
</section>

<section class="card card-back" aria-label="Card back">
  <div class="back-brand"><span class="brand-dot"></span>RIVERBEND ADVISORY</div>

  <div class="person">
    <p class="person-name">Daniel Whitford</p>
    <p class="person-title">Consultant Owner</p>
  </div>

  <ul class="contact">
    <li>
      <span>2716 5th St. S #4372 Arlington,<br>VA 22198</span>
      <svg width="18" height="16" viewBox="0 0 18 16" aria-hidden="true">
        <path d="M9 1 L17 8 H14.5 V15 H11 V10.5 H7 V15 H3.5 V8 H1 Z" fill="var(--red)"/>
      </svg>
    </li>
    <li>
      <span>703-555-0187</span>
      <svg width="18" height="16" viewBox="0 0 18 16" aria-hidden="true">
        <path d="M4 2 C2 4 2 8 6 12 C10 15.5 13 15 15 13 L12.5 10.5 L10.5 12 C8.5 11 6 8.5 5 6.5 L6.5 4.5 Z" fill="var(--red)"/>
      </svg>
    </li>
    <li class="email">
      <span>dwhitford@rvbadv.example</span>
      <svg width="18" height="16" viewBox="0 0 18 16" aria-hidden="true">
        <rect x="1" y="3" width="16" height="11" fill="var(--red)"/>
        <path d="M1 3 L9 9.5 L17 3" fill="none" stroke="#fff" stroke-width="1.3"/>
      </svg>
    </li>
  </ul>

  <svg class="back-bands" width="742" height="423" viewBox="0 0 742 423" aria-hidden="true">
    <rect x="0" y="368" width="742" height="55" fill="var(--navy)"/>
    <path d="M270 395 V370 Q270 344 296 344 H742 V395 Z" fill="var(--white)"/>
    <path d="M276 389 V372 Q276 349 299 349 H742 V389 Z" fill="var(--red)"/>
  </svg>

  <p class="back-web">
    <svg width="22" height="22" viewBox="0 0 22 22" aria-hidden="true">
      <circle cx="11" cy="11" r="10" fill="#fff"/>
      <g fill="none" stroke="var(--red)" stroke-width="1.2">
        <circle cx="11" cy="11" r="6.5"/>
        <ellipse cx="11" cy="11" rx="3" ry="6.5"/>
        <line x1="4.5" y1="11" x2="17.5" y2="11"/>
        <line x1="5.5" y1="7.5" x2="16.5" y2="7.5"/>
        <line x1="5.5" y1="14.5" x2="16.5" y2="14.5"/>
      </g>
    </svg>
    www.rvbadv.example
  </p>
</section>

</body>
</html>
```